"Got Radon?" Banner Ads

I need banner ads made for Pelvaro Banner Circuit campaign. There are 10 sizes of banners, so I need all 10 sizes. All of them can be similar in design and concept, but need to look good and the content must fill the space nicely.

The text on the ad is "Got Radon?" big/bold, and there should be a picture of a house with gas seeping into it from the ground. I have attached an example of an existing ad for reference.

These are the 10 sizes of banners that we need:
970x90
120x600
160x600
200x200
250x250
350x250
300x600
336x280
468x60
728x90

```html
<!DOCTYPE html>
<html lang="en">
<head>
<meta charset="utf-8">
<title>Got Radon? — Pelvaro Banner Circuit banner set</title>
<link rel="stylesheet" href="https://fonts.googleapis.com/css2?family=Montserrat:wght@700;800&display=swap">
<style>
  :root {
    --board: #474747;
    --navy: #0a4a8f;
    --rim: #ffffff;
    --headline: #f7ec13;
    --headline-edge: #3b3a12;
  }
  * { margin: 0; padding: 0; box-sizing: border-box; }
  html, body { width: 1200px; height: 1200px; overflow: hidden; background: var(--board); }
  .board { position: relative; width: 1200px; height: 1200px; }
  .defs { position: absolute; width: 0; height: 0; }

  .banner {
    position: absolute;
    background: var(--navy);
    overflow: hidden;
    box-shadow: 0 1px 3px rgba(0,0,0,.35);
  }
  .banner svg.art { position: absolute; inset: 0; display: block; }
  .scene { stroke: var(--rim); stroke-width: 4; }

  .headline {
    position: absolute;
    left: 0; right: 0;
    font-family: "Montserrat", sans-serif;
    font-weight: 800;
    color: var(--headline);
    text-align: center;
    line-height: 1;
    white-space: nowrap;
    -webkit-text-stroke: 1.2px var(--headline-edge);
    paint-order: stroke fill;
    text-shadow: 0 2px 3px rgba(0,0,0,.35);
  }
  .stack { display: flex; flex-direction: column; align-items: center; transform: translateY(-50%); }
  .stack span { display: block; }
  .line { transform: translateY(-50%); }

  /* banner sizes */
  .b-120x600 { left: 55px;  top: 64px;  width: 117px; height: 584px; }
  .b-160x600 { left: 202px; top: 62px;  width: 158px; height: 584px; }
  .b-200x200 { left: 394px; top: 62px;  width: 217px; height: 217px; }
  .b-250x250 { left: 394px; top: 313px; width: 271px; height: 270px; }
  .b-300x600 { left: 715px; top: 63px;  width: 294px; height: 585px; }
  .b-970x90  { left: 55px;  top: 689px; width: 586px; height: 73px; }
  .b-728x90  { left: 55px;  top: 796px; width: 508px; height: 65px; }
  .b-350x250 { left: 55px;  top: 889px; width: 380px; height: 270px; }
  .b-336x280 { left: 715px; top: 690px; width: 365px; height: 303px; }
  .b-468x60  { left: 715px; top: 1029px; width: 429px; height: 39px; }
</style>
</head>
<body>
<div class="board">

  <svg class="defs" aria-hidden="true">
    <defs>
      <linearGradient id="sky-house-lawn" x1="0" y1="0" x2="0" y2="1">
        <stop offset="0" stop-color="#8db6ea"/>
        <stop offset=".3" stop-color="#b9b6b0"/>
        <stop offset=".55" stop-color="#8fae7a"/>
        <stop offset=".8" stop-color="#45a33a"/>
        <stop offset="1" stop-color="#2e8e2a"/>
      </linearGradient>
      <linearGradient id="tall-scene" x1="0" y1="0" x2="0" y2="1">
        <stop offset="0" stop-color="#a9cde0"/>
        <stop offset=".15" stop-color="#b7bcb6"/>
        <stop offset=".32" stop-color="#7fc46f"/>
        <stop offset=".55" stop-color="#eef3ea"/>
        <stop offset=".72" stop-color="#a9b3b8"/>
        <stop offset=".88" stop-color="#7daa6a"/>
        <stop offset="1" stop-color="#3f9b35"/>
      </linearGradient>
      <linearGradient id="skyscraper-scene" x1="0" y1="0" x2="0" y2="1">
        <stop offset="0" stop-color="#4fbf3c"/>
        <stop offset=".22" stop-color="#9fdc8a"/>
        <stop offset=".42" stop-color="#eef6fb"/>
        <stop offset=".62" stop-color="#a8c9ef"/>
        <stop offset=".78" stop-color="#b5aea6"/>
        <stop offset=".9" stop-color="#6cae56"/>
        <stop offset="1" stop-color="#3a9a30"/>
      </linearGradient>
      <linearGradient id="leader-scene" x1="0" y1="0" x2="1" y2="0">
        <stop offset="0" stop-color="#b3b2ab"/>
        <stop offset=".25" stop-color="#6db55c"/>
        <stop offset=".55" stop-color="#4fae3f"/>
        <stop offset=".8" stop-color="#8fc47f"/>
        <stop offset="1" stop-color="#c4cfc6"/>
      </linearGradient>
    </defs>
  </svg>

  <!-- 120 x 600 -->
  <div class="banner b-120x600">
    <svg class="art" width="117" height="584" viewBox="0 0 117 584">
      <path class="scene" role="img" aria-label="Two houses with green radon gas rising from the lawn" fill="url(#tall-scene)"
            d="M-4,72 C30,42 90,38 121,50 L121,470 C102,528 40,548 -4,534 Z"/>
    </svg>
    <div class="headline stack" style="top:262px">
      <span style="font-size:40px">GOT</span>
      <span style="font-size:22px;margin-top:2px">RADON</span>
      <span style="font-size:40px;margin-top:4px">?</span>
    </div>
  </div>

  <!-- 160 x 600 -->
  <div class="banner b-160x600">
    <svg class="art" width="158" height="584" viewBox="0 0 158 584">
      <path class="scene" role="img" aria-label="Two houses with green radon gas rising from the lawn" fill="url(#tall-scene)"
            d="M-4,150 C10,70 90,35 162,42 L162,470 C140,530 60,545 -4,515 Z"/>
    </svg>
    <div class="headline stack" style="top:262px">
      <span style="font-size:54px">GOT</span>
      <span style="font-size:30px;margin-top:2px">RADON</span>
      <span style="font-size:50px;margin-top:6px">?</span>
    </div>
  </div>

  <!-- 200 x 200 -->
  <div class="banner b-200x200">
    <svg class="art" width="217" height="217" viewBox="0 0 217 217">
      <path class="scene" role="img" aria-label="Brick house with green radon gas seeping from the ground" fill="url(#sky-house-lawn)"
            d="M-4,-4 H221 V180 Q110,214 -4,170 Z"/>
    </svg>
    <div class="headline line" style="top:150px;font-size:24px">GOT RADON?</div>
  </div>

  <!-- 250 x 250 -->
  <div class="banner b-250x250">
    <svg class="art" width="271" height="270" viewBox="0 0 271 270">
      <path class="scene" role="img" aria-label="Brick house with green radon gas seeping from the ground" fill="url(#sky-house-lawn)"
            d="M-4,-4 H275 V221 Q140,262 -4,206 Z"/>
    </svg>
    <div class="headline line" style="top:199px;font-size:28px">GOT RADON?</div>
  </div>

  <!-- 300 x 600 -->
  <div class="banner b-300x600">
    <svg class="art" width="294" height="585" viewBox="0 0 294 585">
      <path class="scene" role="img" aria-label="Green radon cloud above a brick house on a lawn" fill="url(#skyscraper-scene)"
            d="M-4,-4 H298 V503 Q150,545 -4,472 Z"/>
    </svg>
    <div class="headline" style="top:141px;transform:translateY(-50%);font-size:96px">GOT</div>
    <div class="headline" style="top:221px;transform:translateY(-50%);font-size:56px">RADON</div>
    <div class="headline" style="top:297px;transform:translateY(-50%);font-size:80px">?</div>
  </div>

  <!-- 970 x 90 -->
  <div class="banner b-970x90">
    <svg class="art" width="586" height="73" viewBox="0 0 586 73">
      <ellipse class="scene" role="img" aria-label="Houses with green radon gas across a lawn" fill="url(#leader-scene)"
               cx="291" cy="42" rx="272" ry="62"/>
    </svg>
    <div class="headline line" style="top:40px;left:148px;right:auto;width:320px;font-size:36px">GOT RADON?</div>
  </div>

  <!-- 728 x 90 -->
  <div class="banner b-728x90">
    <svg class="art" width="508" height="65" viewBox="0 0 508 65">
      <ellipse class="scene" role="img" aria-label="House with green radon gas across a lawn" fill="url(#leader-scene)"
               cx="251" cy="40" rx="219" ry="56"/>
    </svg>
    <div class="headline line" style="top:38px;left:164px;right:auto;width:300px;font-size:32px">GOT RADON?</div>
  </div>

  <!-- 350 x 250 -->
  <div class="banner b-350x250">
    <svg class="art" width="380" height="270" viewBox="0 0 380 270">
      <path class="scene" role="img" aria-label="White two-storey house with green radon gas seeping from the lawn" fill="url(#sky-house-lawn)"
            d="M-4,-4 H384 V214 Q190,270 -4,202 Z"/>
    </svg>
    <div class="headline line" style="top:187px;font-size:38px">GOT RADON?</div>
  </div>

  <!-- 336 x 280 -->
  <div class="banner b-336x280">
    <svg class="art" width="365" height="303" viewBox="0 0 365 303">
      <path class="scene" role="img" aria-label="Brick house with green radon gas seeping from the ground" fill="url(#sky-house-lawn)"
            d="M-4,-4 H369 V230 Q190,296 -4,236 Z"/>
    </svg>
    <div class="headline line" style="top:206px;font-size:38px">GOT RADON?</div>
  </div>

  <!-- 468 x 60 -->
  <div class="banner b-468x60">
    <svg class="art" width="429" height="39" viewBox="0 0 429 39">
      <ellipse class="scene" role="img" aria-label="Houses with green radon gas across a lawn" fill="url(#leader-scene)"
               cx="212" cy="22" rx="185" ry="32" style="stroke-width:3"/>
    </svg>
    <div class="headline line" style="top:21px;left:113px;right:auto;width:200px;font-size:22px">GOT RADON?</div>
  </div>

</div>
</body>
</html>
```